whitening syringe artwork design

3ml syringe with silkscreen printing:
sample:
https://www.shopvarnex-example.com/Bravo-Nerval-Whitening-Syringes-Carbamide/item/Q47261KD9X/ref=lst_2_4?cid=7PK92LX04QWRT&dflag=1&keywords=whitening+syringes&qid=1598274410&sprefix=whitening+sy%2Caps%2C150&sr=4-2
inside the writing:
"teeth whitening gel " change to "Solivène WHITENING GEL"
"Advanced formula" change to our logo and "Not all gels are created equal. "

additional requirements:
Inches: 2.01" wide x 1.34" around

CM: 5.1cm wide x 3.4cm around

See attached template: Generic_Syringe Labels 3ml_Silkscreen.pdf

- Leave the volume gage where it is, so it prints correctly on the syringe

- Feel free to change the color and font style

- An "identifying marker" is required: Teeth Whitening Syringe or Teeth Whitening Gel (for example)

- Replace "Teeth Whitening Gel - Advanced Formula" with your text and logo - it is there as a placeholder

-We require PDF files created to print ready specifications. Color images should be down-sampled to 300DPI

-Please provide us your Chromidex color references for the color used in your artwork

https://www.chromidex-example.com/color-finder#/pick?chromidexBook=chromidexSolidCoatedV3M2

-Please ensure that all fonts are embedded in the PDF document or make sure you convert fonts to outlines to prevent any issues with fonts (AI-Type-Create Outlines)

We will need your print ready artwork in a high resolution PDF file

Target Market(s)

teeth whitening ecommerce

Requirements
Must have
• follow the guide document, and add text I want, color code from Chromidex is provided

```html
<!DOCTYPE html>
<html lang="en">
<head>
<meta charset="utf-8">
<title>Whitening Syringe Silkscreen Artwork</title>
<link href="https://fonts.googleapis.com/css2?family=Kanit:ital,wght@1,800&family=Montserrat:wght@600&family=Roboto+Condensed:wght@700&display=swap" rel="stylesheet">
<style>
  :root {
    --paper: #ffffff;
    --ink-title: #2a2672;
    --ink-brand: #4a4d52;
    --brand-dot: #f4b9ae;
    --gauge-navy: #1f3a86;
    --gauge-blue: #1c6bb5;
    --band-light: #eeeeee;
    --band-mid: #9a9a9a;
    --band-dark: #333333;
    --band-tail-dark: #7a7a7a;
  }
  html, body {
    margin: 0;
    padding: 0;
    width: 1200px;
    height: 718px;
    overflow: hidden;
    background: var(--paper);
  }
  .artboard { display: block; width: 1200px; height: 718px; }
  .product-title {
    font-family: "Kanit", sans-serif;
    font-style: italic;
    font-weight: 800;
    fill: var(--ink-title);
  }
  .brand-name {
    font-family: "Montserrat", sans-serif;
    font-weight: 600;
    fill: var(--ink-brand);
    letter-spacing: 6px;
  }
  .brand-dot { fill: var(--brand-dot); }
  .gauge-mark {
    stroke: var(--gauge-navy);
    stroke-width: 2.6;
    fill: none;
  }
  .gauge-label {
    font-family: "Roboto Condensed", sans-serif;
    font-weight: 700;
    fill: var(--gauge-navy);
  }
  .gauge-unit {
    font-family: "Montserrat", sans-serif;
    font-weight: 600;
    fill: var(--gauge-navy);
  }
  .stop-light { stop-color: var(--band-light); }
  .stop-mid { stop-color: var(--band-mid); }
  .stop-dark { stop-color: var(--band-dark); }
  .stop-tail { stop-color: var(--band-tail-dark); }
</style>
</head>
<body>
<svg class="artboard" viewBox="0 0 1200 718" xmlns="http://www.w3.org/2000/svg">
  <defs>
    <linearGradient id="bandMain" x1="0" x2="1" y1="0" y2="0">
      <stop offset="0" class="stop-mid"/>
      <stop offset="0.3" class="stop-light"/>
      <stop offset="0.6" class="stop-dark"/>
      <stop offset="0.85" class="stop-light"/>
      <stop offset="1" class="stop-light"/>
    </linearGradient>
    <linearGradient id="bandTail" x1="0" x2="1" y1="0" y2="0">
      <stop offset="0" class="stop-light"/>
      <stop offset="0.6" class="stop-light"/>
      <stop offset="1" class="stop-tail"/>
    </linearGradient>
  </defs>

  <g class="label label--pen-upper">
    <text class="product-title" x="110" y="198" font-size="52" textLength="455" lengthAdjust="spacingAndGlyphs">Orla Whitening Pen</text>
    <polygon points="110,202 423,202 427,211 106,211" fill="url(#bandMain)"/>
    <polygon points="473,202 559,202 555,211 469,211" fill="url(#bandTail)"/>
    <text class="brand-name" x="332" y="239" font-size="26" text-anchor="middle">VANTELL</text>
    <circle class="brand-dot" cx="331" cy="255" r="8"/>
  </g>

  <g class="label label--pen-lower">
    <text class="product-title" x="100" y="490" font-size="52" textLength="456" lengthAdjust="spacingAndGlyphs">Orla Whitening Pen</text>
    <polygon points="100,495 413,495 418,503 96,503" fill="url(#bandMain)"/>
    <polygon points="463,495 550,495 546,503 459,503" fill="url(#bandTail)"/>
    <text class="brand-name" x="332" y="531" font-size="26" text-anchor="middle">VANTELL</text>
    <circle class="brand-dot" cx="331" cy="547" r="8"/>
  </g>

  <g class="label label--gel">
    <text class="product-title" x="710" y="256" font-size="41" textLength="360" lengthAdjust="spacingAndGlyphs">Teeth Whitening Gel</text>
    <polygon points="713,259 961,259 965,265 710,265" fill="url(#bandMain)"/>
    <polygon points="1001,259 1066,259 1063,265 997,265" fill="url(#bandTail)"/>
    <text class="brand-name" x="900" y="290" font-size="22" text-anchor="middle" style="letter-spacing:5px">VANTELL</text>
    <circle class="brand-dot" cx="899" cy="304" r="7"/>
  </g>

  <g class="volume-gauge">
    <line class="gauge-mark" x1="662" y1="378" x2="662" y2="440"/>
    <line class="gauge-mark" x1="731" y1="403" x2="731" y2="440"/>
    <line class="gauge-mark" x1="800" y1="378" x2="800" y2="440"/>
    <line class="gauge-mark" x1="879" y1="403" x2="879" y2="440"/>
    <line class="gauge-mark" x1="957" y1="378" x2="957" y2="440"/>
    <line class="gauge-mark" x1="1026" y1="403" x2="1026" y2="440"/>
    <line class="gauge-mark" x1="1095" y1="378" x2="1095" y2="440"/>

    <text class="gauge-label" font-size="20" text-anchor="middle" transform="translate(736,372) rotate(-90)">½</text>
    <text class="gauge-label" font-size="24" text-anchor="middle" transform="translate(806,363) rotate(-90)">1</text>
    <text class="gauge-label" font-size="24" text-anchor="middle" transform="translate(885,376) rotate(-90)">1½</text>
    <text class="gauge-label" font-size="24" text-anchor="middle" transform="translate(963,363) rotate(-90)">2</text>
    <text class="gauge-label" font-size="24" text-anchor="middle" transform="translate(1032,377) rotate(-90)">2½</text>
    <text class="gauge-label" font-size="24" text-anchor="middle" transform="translate(1101,363) rotate(-90)">3</text>
    <text class="gauge-unit" font-size="17" text-anchor="middle" transform="translate(1116,410) rotate(-90)">ml/cc</text>
  </g>
</svg>
</body>
</html>
```